Would like to reproduce this screen to look more modern

My app is a place for farmers to post jobs a when needing help around the Farm, and local farmhands can apply for the job. The Farmer can then review multiple applicants and select the one best fit for the task at hand. I'm trying to give my screens an updated look while keeping my current color scheme and flow. I would like for you guys to recreate this screen with an updated look the best you can. The main screen with the PX will stay the same. I put that in there to show our logo and our main colors. They look outdated. the other 2 screens are looking at the customers profile, and the screen that u fill out to post a new job.

Target Market(s)

Farmers and farm employees inside the US

Industry/Entity Type

Agriculture

Requirements
Must have
• the same components for the flow but a new look
Nice to have
• ...
Should not have
• Should not change any features, but we can change how buttons look

```html
<!DOCTYPE html>
<html lang="en">
<head>
<meta charset="utf-8">
<title>Farm Jobs – Home</title>
<link href="https://fonts.googleapis.com/css2?family=Inter:wght@400;500;600;700&display=swap" rel="stylesheet">
<style>
:root{
  --canvas:#ffffff;
  --green-dark:#5f9440;
  --green:#74a84e;
  --green-light:#8cc063;
  --accent:#7cbf4e;
  --home-pill:#c9ef8c;
  --sheet:#f5f5f5;
  --card:#ffffff;
  --ink:#2b2b2b;
  --muted:#8f8f8f;
  --faint:#c4c4c4;
  --heart:#f03c3c;
  --orange:#f08a3a; --orange-bg:#fff3ea;
  --blue:#3595e2;   --blue-bg:#eef5fd;
  --lime:#7db844;   --lime-bg:#f3f8ee;
  --violet:#4a3d9e; --violet-bg:#f1f0fa;
  --yellow:#dccd25; --yellow-bg:#fcfbe8;
}
*{box-sizing:border-box;margin:0;padding:0}
html,body{width:1169px;height:1200px;overflow:hidden;background:var(--canvas);font-family:"Inter",sans-serif;color:var(--ink)}
.screen{position:absolute;width:302px;height:654px;border-radius:34px;overflow:hidden;background:var(--sheet)}
.screen--create{left:190px;top:427px}
.screen--list{left:625px;top:152px}
.header{position:absolute;left:0;top:0;width:100%;background:linear-gradient(160deg,var(--green-light) 0%,var(--green) 45%,var(--green-dark) 100%)}
.screen--create .header{height:240px}
.screen--list .header{height:120px}
.sheet{position:absolute;left:0;right:0;bottom:0;background:var(--sheet);border-radius:26px 26px 0 0}
.screen--create .sheet{top:209px}
.screen--list .sheet{top:87px}
.avatar{position:absolute;width:34px;height:34px;border-radius:50%;background:linear-gradient(135deg,#e9e9e9,#9a9a9a);border:2px solid #fff}
.user{position:absolute;color:#fff}
.user h1{font-size:13.5px;font-weight:700;letter-spacing:-.2px;line-height:16px}
.user p{font-size:8.5px;line-height:11px;opacity:.95}
.head-icon{position:absolute;width:16px;height:16px}
.create-btn{position:absolute;left:118px;top:93px;width:66px;height:66px;border-radius:50%;background:#fff;box-shadow:0 6px 16px rgba(0,0,0,.12)}
.create-label{position:absolute;left:0;width:100%;top:167px;text-align:center;color:#fff;font-size:9.5px}
.add-mini{position:absolute;width:15px;height:15px;border-radius:50%;background:#fff}
.tabs{position:absolute;left:0;width:100%;font-size:10.5px;font-weight:600}
.tabs span{position:absolute;top:0;white-space:nowrap}
.tab-active{color:var(--ink)}
.tab-idle{color:var(--faint)}
.tab-bar{position:absolute;top:19px;height:3px;width:61px;border-radius:2px;background:var(--accent)}
.search{position:absolute;left:12px;width:252px;height:32px;border-radius:16px;background:#fff;font-size:10.5px;color:var(--faint);display:flex;align-items:center;padding-left:12px;gap:6px}
.filter{position:absolute;left:276px;width:16px;height:16px}
.job{position:absolute;left:12px;width:276px;height:68px;border-radius:10px;background:var(--card)}
.dates{position:absolute;left:8px;top:7px;width:53px;height:54px;border-radius:9px;display:flex;flex-direction:column;align-items:center;justify-content:center;font-size:9.3px;font-weight:600;line-height:12px}
.dates .to{font-size:6px;line-height:9px;display:flex;align-items:center;gap:2px}
.dates .to::before,.dates .to::after{content:"";width:7px;height:1px;background:currentColor;opacity:.6}
.orange{color:var(--orange);background:var(--orange-bg)}
.blue{color:var(--blue);background:var(--blue-bg)}
.lime{color:var(--lime);background:var(--lime-bg)}
.violet{color:var(--violet);background:var(--violet-bg)}
.yellow{color:var(--yellow);background:var(--yellow-bg)}
.info{position:absolute;left:68px;top:9px;width:146px}
.info h3{font-size:8.4px;font-weight:400;line-height:13px;letter-spacing:-.15px;white-space:nowrap}
.info p{font-size:7.4px;color:var(--muted);line-height:12px;display:flex;align-items:center;gap:3px;white-space:nowrap}
.info p::before{content:"";width:3px;height:3px;border-radius:50%;background:var(--faint)}
.rate{position:absolute;right:8px;top:19px;width:58px;text-align:center}
.rate strong{display:block;font-size:15.5px;font-weight:600;line-height:19px;color:#3a3a3a;letter-spacing:-.2px}
.rate span{font-size:7.6px;color:var(--muted)}
.heart{position:absolute;right:7px;top:5px;width:11px;height:10px}
.list{position:absolute;left:0;right:0;top:0;bottom:46px;overflow:hidden}
.nav{position:absolute;left:0;bottom:0;width:100%;height:60px;background:#fff;border-radius:22px 22px 0 0;box-shadow:0 -4px 14px rgba(0,0,0,.04)}
.nav-home{position:absolute;left:22px;top:6px;width:30px;height:30px;border-radius:50%;background:var(--home-pill);display:flex;align-items:center;justify-content:center}
.nav-icon{position:absolute;top:13px;width:16px;height:16px}
.home-bar{position:absolute;left:99px;bottom:7px;width:103px;height:4px;border-radius:2px;background:#111}
</style>
</head>
<body>

<!-- Home with create action -->
<section class="screen screen--create">
  <div class="header"></div>
  <div class="avatar" style="left:12px;top:34px" role="img" aria-label="Profile photo of the farmer"></div>
  <div class="user" style="left:54px;top:38px"><h1>Daniel Hartwell</h1><p>5550148230</p></div>
  <svg class="head-icon" style="left:249px;top:40px" viewBox="0 0 16 16" fill="none" stroke="#fff" stroke-width="1.3"><path d="M4 11V7a4 4 0 0 1 8 0v4l1 1.5H3z"/><path d="M6.5 14h3"/><circle cx="11.5" cy="3.5" r="1.6" fill="var(--heart)" stroke="none"/></svg>
  <svg class="head-icon" style="left:278px;top:40px" viewBox="0 0 16 16" stroke="#fff" stroke-width="1.3"><path d="M2 5h12M7 10h7"/></svg>
  <div class="create-btn"><svg viewBox="0 0 66 66" width="66" height="66" stroke="var(--green)" stroke-width="1.6"><path d="M33 22v22M22 33h22"/></svg></div>
  <p class="create-label">Tap to Create New Job</p>

  <div class="sheet">
    <div class="tabs" style="top:15px">
      <span class="tab-active" style="left:42px">Current Jobs For You</span>
      <span class="tab-idle" style="left:166px">Nearby Farmhands</span>
      <i class="tab-bar" style="left:59px"></i>
    </div>
    <div class="search" style="top:54px"><svg width="10" height="10" viewBox="0 0 10 10" fill="none" stroke="#b5b5b5" stroke-width="1"><circle cx="4.2" cy="4.2" r="3.2"/><path d="M6.6 6.6 9.2 9.2"/></svg>Search</div>
    <svg class="filter" style="top:62px" viewBox="0 0 16 16" fill="none" stroke="var(--green)" stroke-width="1"><path d="M1 3h14M1 8h14M1 13h14"/><rect x="9" y="1.5" width="3" height="3" fill="#fff"/><rect x="4" y="6.5" width="3" height="3" fill="#fff"/><rect x="8" y="11.5" width="3" height="3" fill="#fff"/></svg>
    <div class="list" style="top:106px">
      <article class="job" style="top:0">
        <div class="dates orange"><b>01 APR</b><span class="to">TO</span><b>15 APR</b></div>
        <div class="info"><h3>Seasonal Farm Labor</h3><p>Dewitt, Lowa</p><p>2.92 miles</p><p>08:00 am - 08:00 pm</p></div>
        <div class="rate"><strong>$12-20</strong><span>Hourly Rate</span></div>
        <svg class="heart" viewBox="0 0 12 11"><path d="M6 10.5 1.2 5.8A2.9 2.9 0 0 1 6 2a2.9 2.9 0 0 1 4.8 3.8z" fill="var(--heart)"/></svg>
      </article>
      <article class="job" style="top:82px">
        <div class="dates blue"><b>01 MAR</b><span class="to">TO</span><b>02 MAR</b></div>
        <div class="info"><h3>Truck Driver</h3><p>Davenport, Lowa</p><p>12.38 miles</p><p>10:00 am - 03:00 pm</p></div>
        <div class="rate"><strong>$15-25</strong><span>Hourly Rate</span></div>
        <svg class="heart" viewBox="0 0 12 11"><path d="M6 10.5 1.2 5.8A2.9 2.9 0 0 1 6 2a2.9 2.9 0 0 1 4.8 3.8z" fill="none" stroke="var(--faint)" stroke-width=".8"/></svg>
      </article>
      <article class="job" style="top:164px">
        <div class="dates lime"><b>31 JAN</b><span class="to">TO</span><b>25 FEB</b></div>
        <div class="info"><h3>Farm Hand, Sprayer, Truck, Repair</h3><p>Dewitt, Lowa</p><p>2.92 miles</p><p>10:00 am - 05:00 pm</p></div>
        <div class="rate"><strong>$17-22</strong><span>Hourly Rate</span></div>
        <svg class="heart" viewBox="0 0 12 11"><path d="M6 10.5 1.2 5.8A2.9 2.9 0 0 1 6 2a2.9 2.9 0 0 1 4.8 3.8z" fill="none" stroke="var(--faint)" stroke-width=".8"/></svg>
      </article>
      <article class="job" style="top:246px">
        <div class="dates violet"><b>27 MAR</b><span class="to">TO</span><b>27 MAR</b></div>
        <div class="info"><h3>Sort and Load Pigs</h3><p>Dewitt, Lowa</p><p>2.92 miles</p><p>08:00 am - 08:00 pm</p></div>
        <div class="rate"><strong>$10-20</strong><span>Hourly Rate</span></div>
        <svg class="heart" viewBox="0 0 12 11"><path d="M6 10.5 1.2 5.8A2.9 2.9 0 0 1 6 2a2.9 2.9 0 0 1 4.8 3.8z" fill="var(--heart)"/></svg>
      </article>
    </div>
  </div>

  <nav class="nav">
    <div class="nav-home"><svg width="15" height="15" viewBox="0 0 16 16" fill="none" stroke="#1f3a12" stroke-width="1.5"><path d="M2 7.5 8 2l6 5.5V14H2z"/><path d="M6.5 14v-4h3v4"/></svg></div>
    <svg class="nav-icon" style="left:90px" viewBox="0 0 16 16" fill="none" stroke="#a9a9a9" stroke-width="1.2"><circle cx="6.5" cy="6.5" r="4.5"/><path d="M10 10l4.5 4.5"/></svg>
    <svg class="nav-icon" style="left:146px" viewBox="0 0 16 16" fill="none" stroke="#a9a9a9" stroke-width="1.1"><rect x="1.5" y="2" width="13" height="12" rx="1.5"/><path d="M4 6h8M4 8.5h8M4 11h5"/></svg>
    <svg class="nav-icon" style="left:202px" viewBox="0 0 16 16" fill="none" stroke="#a9a9a9" stroke-width="1.1"><path d="M4.5 9V5a1 1 0 0 1 2 0v3V3a1 1 0 0 1 2 0v5V4a1 1 0 0 1 2 0v5l1-1.5a1 1 0 0 1 1.6 1.2L11 13.5a3 3 0 0 1-2.5 1.5H7a3 3 0 0 1-3-3z"/></svg>
    <svg class="nav-icon" style="left:258px" viewBox="0 0 16 16" fill="none" stroke="#a9a9a9" stroke-width="1.1"><rect x="1.5" y="3" width="13" height="11" rx="1.5"/><path d="M1.5 6.5h13M5 1.5v3M11 1.5v3M4.5 9h1M7.5 9h1M10.5 9h1M4.5 11.5h1M7.5 11.5h1M10.5 11.5h1"/></svg>
    <i class="home-bar"></i>
  </nav>
</section>

<!-- Home, job list -->
<section class="screen screen--list">
  <div class="header"></div>
  <div class="avatar" style="left:13px;top:42px" role="img" aria-label="Profile photo of the farmer"></div>
  <div class="user" style="left:54px;top:45px"><h1>Daniel Hartwell</h1><p>5550148230</p></div>
  <div class="add-mini" style="left:221px;top:50px"><svg width="15" height="15" viewBox="0 0 15 15" stroke="var(--green)" stroke-width="1.3"><path d="M7.5 4.5v6M4.5 7.5h6"/></svg></div>
  <svg class="head-icon" style="left:248px;top:49px" viewBox="0 0 16 16" fill="none" stroke="#fff" stroke-width="1.3"><path d="M4 11V7a4 4 0 0 1 8 0v4l1 1.5H3z"/><path d="M6.5 14h3"/><circle cx="11.5" cy="3.5" r="1.6" fill="var(--heart)" stroke="none"/></svg>
  <svg class="head-icon" style="left:277px;top:49px" viewBox="0 0 16 16" stroke="#fff" stroke-width="1.3"><path d="M2 5h12M7 10h7"/></svg>

  <div class="sheet">
    <div class="tabs" style="top:19px">
      <span class="tab-active" style="left:43px">Current Jobs For You</span>
      <span class="tab-idle" style="left:166px">Nearby Farmhands</span>
      <i class="tab-bar" style="left:60px"></i>
    </div>
    <div class="search" style="top:55px"><svg width="10" height="10" viewBox="0 0 10 10" fill="none" stroke="#b5b5b5" stroke-width="1"><circle cx="4.2" cy="4.2" r="3.2"/><path d="M6.6 6.6 9.2 9.2"/></svg>Search</div>
    <svg class="filter" style="top:63px" viewBox="0 0 16 16" fill="none" stroke="var(--green)" stroke-width="1"><path d="M1 3h14M1 8h14M1 13h14"/><rect x="9" y="1.5" width="3" height="3" fill="#fff"/><rect x="4" y="6.5" width="3" height="3" fill="#fff"/><rect x="8" y="11.5" width="3" height="3" fill="#fff"/></svg>
    <div class="list" style="top:108px">
      <article class="job" style="top:0">
        <div class="dates orange"><b>01 APR</b><span class="to">TO</span><b>15 APR</b></div>
        <div class="info"><h3>Seasonal Farm Labor</h3><p>Dewitt, Lowa</p><p>2.92 miles</p><p>08:00 am - 08:00 pm</p></div>
        <div class="rate"><strong>$12-20</strong><span>Hourly Rate</span></div>
        <svg class="heart" viewBox="0 0 12 11"><path d="M6 10.5 1.2 5.8A2.9 2.9 0 0 1 6 2a2.9 2.9 0 0 1 4.8 3.8z" fill="var(--heart)"/></svg>
      </article>
      <article class="job" style="top:82px">
        <div class="dates blue"><b>01 MAR</b><span class="to">TO</span><b>02 MAR</b></div>
        <div class="info"><h3>Truck Driver</h3><p>Davenport, Lowa</p><p>12.38 miles</p><p>10:00 am - 03:00 pm</p></div>
        <div class="rate"><strong>$15-25</strong><span>Hourly Rate</span></div>
        <svg class="heart" viewBox="0 0 12 11"><path d="M6 10.5 1.2 5.8A2.9 2.9 0 0 1 6 2a2.9 2.9 0 0 1 4.8 3.8z" fill="none" stroke="var(--faint)" stroke-width=".8"/></svg>
      </article>
      <article class="job" style="top:163px">
        <div class="dates lime"><b>31 JAN</b><span class="to">TO</span><b>25 FEB</b></div>
        <div class="info"><h3>Farm Hand, Sprayer, Truck, Repair</h3><p>Dewitt, Lowa</p><p>2.92 miles</p><p>10:00 am - 05:00 pm</p></div>
        <div class="rate"><strong>$17-22</strong><span>Hourly Rate</span></div>
        <svg class="heart" viewBox="0 0 12 11"><path d="M6 10.5 1.2 5.8A2.9 2.9 0 0 1 6 2a2.9 2.9 0 0 1 4.8 3.8z" fill="none" stroke="var(--faint)" stroke-width=".8"/></svg>
      </article>
      <article class="job" style="top:245px">
        <div class="dates violet"><b>27 MAR</b><span class="to">TO</span><b>27 MAR</b></div>
        <div class="info"><h3>Sort and Load Pigs</h3><p>Dewitt, Lowa</p><p>2.92 miles</p><p>08:00 am - 08:00 pm</p></div>
        <div class="rate"><strong>$10-20</strong><span>Hourly Rate</span></div>
        <svg class="heart" viewBox="0 0 12 11"><path d="M6 10.5 1.2 5.8A2.9 2.9 0 0 1 6 2a2.9 2.9 0 0 1 4.8 3.8z" fill="var(--heart)"/></svg>
      </article>
      <article class="job" style="top:326px">
        <div class="dates yellow"><b>13 JUL</b><span class="to">TO</span><b>14 JUL</b></div>
        <div class="info"><h3>Need Help Bailing Hay, small squares</h3><p>Alabaster, Alabama</p><p>5118 miles</p><p>06:00 am - 05:00 pm</p></div>
        <div class="rate"><strong>$20-25</strong><span>Hourly Rate</span></div>
        <svg class="heart" viewBox="0 0 12 11"><path d="M6 10.5 1.2 5.8A2.9 2.9 0 0 1 6 2a2.9 2.9 0 0 1 4.8 3.8z" fill="none" stroke="var(--faint)" stroke-width=".8"/></svg>
      </article>
    </div>
  </div>

  <nav class="nav">
    <div class="nav-home"><svg width="15" height="15" viewBox="0 0 16 16" fill="none" stroke="#1f3a12" stroke-width="1.5"><path d="M2 7.5 8 2l6 5.5V14H2z"/><path d="M6.5 14v-4h3v4"/></svg></div>
    <svg class="nav-icon" style="left:90px" viewBox="0 0 16 16" fill="none" stroke="#a9a9a9" stroke-width="1.2"><circle cx="6.5" cy="6.5" r="4.5"/><path d="M10 10l4.5 4.5"/></svg>
    <svg class="nav-icon" style="left:146px" viewBox="0 0 16 16" fill="none" stroke="#a9a9a9" stroke-width="1.1"><rect x="1.5" y="2" width="13" height="12" rx="1.5"/><path d="M4 6h8M4 8.5h8M4 11h5"/></svg>
    <svg class="nav-icon" style="left:202px" viewBox="0 0 16 16" fill="none" stroke="#a9a9a9" stroke-width="1.1"><path d="M4.5 9V5a1 1 0 0 1 2 0v3V3a1 1 0 0 1 2 0v5V4a1 1 0 0 1 2 0v5l1-1.5a1 1 0 0 1 1.6 1.2L11 13.5a3 3 0 0 1-2.5 1.5H7a3 3 0 0 1-3-3z"/></svg>
    <svg class="nav-icon" style="left:258px" viewBox="0 0 16 16" fill="none" stroke="#a9a9a9" stroke-width="1.1"><rect x="1.5" y="3" width="13" height="11" rx="1.5"/><path d="M1.5 6.5h13M5 1.5v3M11 1.5v3M4.5 9h1M7.5 9h1M10.5 9h1M4.5 11.5h1M7.5 11.5h1M10.5 11.5h1"/></svg>
    <i class="home-bar"></i>
  </nav>
</section>

</body>
</html>
```